Flyer informing about the activities of people in action

Wege im Wandel (www.wegeimwandel-beispiel.ch) offers coaching, medation, support for traumatized people and conflict and crisis intervention. The flyer should inform about the activities in a plain and simple way (see logo on the homepage).

Target Market(s)

Adults who live in Switzerland or Germany

Requirements
Must have
• - simple flyer, the design is based on my logo. Brief information about my offer, reference to my homepage www.wegeimwandel-beispiel.
- 2-sided: on the first page - fire circle with text (see homepage - Home), on the back - offer with logo
- possibly a square flyer

Should not have
• no photos

```html
<!DOCTYPE html>
<html lang="en">
<head>
<meta charset="utf-8">
<title>Wege im Wandel – Flyer</title>
<link href="https://fonts.googleapis.com/css2?family=Arimo:ital,wght@0,400;0,700;1,400&family=Open+Sans:wght@600;700&family=Roboto+Condensed:wght@300;400&display=swap" rel="stylesheet">
<style>
  :root {
    --backdrop: #f3f0f0;
    --paper: #ffffff;
    --sun: #fae197;
    --sun-wash: rgba(250, 225, 151, 0.42);
    --sun-clear: rgba(250, 225, 151, 0);
    --ink: #111111;
    --ink-grey: #555555;
    --ink-light: #8a8a8a;
    --rule: #222222;
    --brand-gold: #a88446;
    --brand-teal: #2f6f68;
  }
  * { box-sizing: border-box; margin: 0; padding: 0; }
  html, body { width: 848px; height: 1200px; overflow: hidden; }
  body { background: var(--backdrop); font-family: "Arimo", Arial, sans-serif; color: var(--ink); position: relative; }

  .page {
    position: absolute;
    background: var(--paper);
    box-shadow: 0 2px 8px rgba(0,0,0,0.12);
    overflow: hidden;
  }

  /* Front page */
  .front { left: 209px; top: 145px; width: 430px; height: 430px; }
  .front__wash {
    position: absolute; left: 0; top: 0; width: 430px; height: 325px;
    background: radial-gradient(closest-side at 50% 50%, var(--sun-wash) 0%, rgba(250,225,151,0.22) 55%, var(--sun-clear) 100%);
  }
  .front__headline { position: absolute; left: 0; right: 0; top: 136px; text-align: center; }
  .front__kicker { font-size: 24px; font-weight: 700; color: var(--ink-grey); line-height: 28px; letter-spacing: 0.3px; }
  .front__title { font-size: 27px; font-weight: 400; color: var(--ink); line-height: 32px; }
  .front__sub { font-size: 17px; font-weight: 700; color: var(--ink-light); line-height: 20px; }
  .front__band { position: absolute; left: 0; right: 0; bottom: 0; height: 105px; background: var(--sun); text-align: center; }
  .front__band-title { font-family: "Open Sans", sans-serif; font-weight: 700; font-size: 14.5px; margin-top: 18px; line-height: 20px; }
  .front__band-rule { width: 363px; height: 1px; background: var(--rule); margin: 2px auto 2px; }
  .front__band-text { font-size: 15.5px; line-height: 17.5px; color: #222; }

  /* Back page */
  .back { left: 206px; top: 624px; width: 433px; height: 433px; background: var(--sun); }
  .back__header { position: absolute; left: 0; top: 0; width: 100%; height: 96px; background: var(--paper); }
  .back__lead {
    position: absolute; left: 22px; top: 28px;
    font-family: "Roboto Condensed", sans-serif; font-weight: 300; font-size: 20px; line-height: 24px; color: var(--ink-grey);
  }
  .brand { position: absolute; left: 306px; top: 41px; display: flex; align-items: center; gap: 5px; }
  .brand__dot { width: 10px; height: 10px; border-radius: 50%; background: var(--brand-teal); }
  .brand__name { font-family: "Roboto Condensed", sans-serif; font-weight: 400; font-size: 15px; line-height: 18px; color: var(--brand-gold); white-space: nowrap; }

  .offer { position: absolute; left: 0; width: 100%; padding-left: 20px; padding-right: 66px; }
  .offer::before { content: ""; position: absolute; left: 0; top: 3px; width: 9px; height: 12px; background: var(--ink); }
  .offer--coaching { top: 119px; }
  .offer--mediation { top: 209px; }
  .offer--trauma { top: 306px; padding-right: 56px; }
  .offer__title { font-family: "Open Sans", sans-serif; font-weight: 600; font-size: 15.5px; line-height: 18px; margin-bottom: 2px; white-space: nowrap; }
  .offer__text { font-size: 11px; line-height: 13px; color: #222; margin-bottom: 5px; }
  .offer__note { font-size: 8.4px; line-height: 10.5px; font-style: italic; color: #222; }
  .back__bar { position: absolute; left: 65px; top: 398px; width: 305px; height: 6px; background: rgba(255,255,255,0.45); }
</style>
</head>
<body>

<section class="page front">
  <div class="front__wash" role="img" aria-label="Soft yellow brush circle decoration behind the headline"></div>
  <div class="front__headline">
    <p class="front__kicker">YOU WANT</p>
    <h1 class="front__title">Solve your stressful situation</h1>
    <p class="front__sub">Clarify your important questions</p>
  </div>
  <div class="front__band">
    <h2 class="front__band-title">Get ahead easier</h2>
    <div class="front__band-rule"></div>
    <p class="front__band-text">In the frustrating collaboration or your<br>laborious life (together)</p>
  </div>
</section>

<section class="page back">
  <header class="back__header">
    <p class="back__lead">I will accompany you and bring you<br>Orientation, clarity and support.</p>
    <div class="brand">
      <span class="brand__dot"></span>
      <span class="brand__name">Wege im Wandel</span>
    </div>
  </header>

  <article class="offer offer--coaching">
    <h3 class="offer__title">Coaching</h3>
    <p class="offer__text">Sometimes you need a counterpart to clarify your own situation or to discover new perspectives and options for action.</p>
    <p class="offer__note">Possible questions: Where are you today and where do you want to be? Do you use your room for maneuver and your skills? What makes you happy</p>
  </article>
  <article class="offer offer--mediation">
    <h3 class="offer__title">Mediation</h3>
    <p class="offer__text">You can no longer resolve certain conflicts yourself. Few words ignite a bitter argument or create an icy silence.</p>
    <p class="offer__note">Possible questions: How are you heard? Do you see the other person's point of view? How do you find something of your lost trust? How do you get back into conversation to find the necessary solutions together?</p>
  </article>
  <article class="offer offer--trauma">
    <h3 class="offer__title">Accompanying traumatized people</h3>
    <p class="offer__text">Their life often feels heavy, oppressive, and joyless. You have tried unsuccessfully to free yourself from this lack of contact and perspective.</p>
    <p class="offer__note">This accompaniment is initially about creating a safe framework in which contact is possible and can be maintained later.</p>
  </article>
  <div class="back__bar"></div>
</section>

</body>
</html>
```